We need a laundry sheet packingbox desgin

-look at our website plooimoes.nl to be in line with our house style/collor
We are a perfume seller and would like to offer also wasshingsheets with NO SMELL, so the customers can buy this incombination with our washingperfumes.
-the wassingheets will be neutrale(NO SMELL)
-it will be for the Dutch market
The next points should be on the desgin of the package
-our brand name: PLOOIMOES
-product name: WASSTRIPS
-(contains) Bevat: 30 wasstrips
-30 wasstrips = 60 wasbeurten
Please take some inspiration of others sellers & regarding eco friendly symbols etc.:
velunta.com & doxamp.nl
Backside information will be provided afther we found the right desgin
Please look at attachement pdf open box.
Here you can find the pdf design where you need to customize:
https://fy.qo/t-Lr8KxPq2Zh

```html
<!DOCTYPE html>
<html lang="nl">
<head>
<meta charset="utf-8">
<title>PLOOIMOES Wasstrips – verpakking</title>
<link rel="stylesheet" href="https://fonts.googleapis.com/css2?family=Josefin+Sans:wght@700&family=Montserrat:wght@400;700&display=swap">
<style>
  :root {
    --olive: #4a5444;
    --olive-deep: #46503f;
    --tan: #7c705a;
    --cutline: #7a6e57;
    --lemon: #ede577;
    --gold: #d9b94a;
    --bronze: #a07a4a;
    --ink: #111111;
    --paper: #ffffff;
    --arrow: #e0201a;
  }
  html, body {
    margin: 0;
    padding: 0;
    width: 1200px;
    height: 1200px;
    overflow: hidden;
    background: var(--paper);
  }
  .canvas {
    position: relative;
    width: 1200px;
    height: 1200px;
  }
  .dieline-sheet {
    position: absolute;
    left: 0;
    top: 0;
    width: 1200px;
    height: 681px;
  }
  .brand-stage {
    position: absolute;
    left: 0;
    top: 681px;
    width: 1200px;
    height: 519px;
    background: var(--olive);
  }
  .spec-label {
    font-family: "Montserrat", sans-serif;
    font-weight: 400;
    fill: var(--ink);
  }
  .brand-word {
    font-family: "Josefin Sans", sans-serif;
    font-weight: 700;
  }
  .pack-count {
    font-family: "Montserrat", sans-serif;
    font-weight: 400;
    fill: var(--gold);
  }
  .panel-copy {
    font-family: "Montserrat", sans-serif;
    font-weight: 700;
    fill: var(--paper);
  }
</style>
</head>
<body>
<div class="canvas">

  <svg class="dieline-sheet" viewBox="0 0 1200 681" xmlns="http://www.w3.org/2000/svg">
    <defs>
      <linearGradient id="gold-type" x1="0" y1="0" x2="1" y2="0">
        <stop offset="0" stop-color="#f2de79"/>
        <stop offset="0.5" stop-color="#b98a2e"/>
        <stop offset="1" stop-color="#f2de79"/>
      </linearGradient>
    </defs>

    <!-- spec heading -->
    <text class="spec-label" x="297" y="18" font-size="18">DIMANTION 1 MM</text>

    <!-- top flaps -->
    <path class="flap flap--side-top" d="M114,107 L118,50 Q119,44 126,44 L166,44 Q173,44 174,52 L178,100 L181,107 Z" fill="var(--paper)" stroke="var(--cutline)" stroke-width="2"/>
    <path class="flap flap--dust-top" d="M184,107 L188,52 Q190,44 200,44 L478,44 Q488,44 490,52 L494,107 Z" fill="var(--paper)" stroke="var(--cutline)" stroke-width="2"/>
    <g class="flap-perforation" stroke="#555" stroke-width="1.5" stroke-dasharray="2 2">
      <line x1="224" y1="62" x2="224" y2="92"/><line x1="242" y1="62" x2="242" y2="92"/>
      <line x1="260" y1="62" x2="260" y2="92"/><line x1="277" y1="62" x2="277" y2="92"/>
      <line x1="295" y1="62" x2="295" y2="92"/><line x1="313" y1="62" x2="313" y2="92"/>
      <line x1="331" y1="62" x2="331" y2="92"/><line x1="349" y1="62" x2="349" y2="92"/>
      <line x1="366" y1="62" x2="366" y2="92"/><line x1="384" y1="62" x2="384" y2="92"/>
      <line x1="402" y1="62" x2="402" y2="92"/><line x1="420" y1="62" x2="420" y2="92"/>
      <line x1="438" y1="62" x2="438" y2="92"/><line x1="455" y1="62" x2="455" y2="92"/>
      <line x1="473" y1="62" x2="473" y2="92"/>
    </g>
    <path class="flap flap--tuck-top" d="M498,107 L502,52 Q503,44 512,44 L544,44 Q554,44 555,54 L559,107 Z" fill="var(--olive)" stroke="var(--cutline)" stroke-width="2"/>
    <path class="lid lid--top" d="M572,38 L864,38 L876,107 L566,107 Z" fill="var(--olive)" stroke="var(--cutline)" stroke-width="2"/>
    <rect class="name-pill" x="616" y="54" width="218" height="41" rx="14" fill="var(--lemon)"/>
    <text class="brand-word" x="725" y="85" font-size="32" text-anchor="middle" fill="var(--ink)">PLOOIMOES</text>

    <!-- side glue panel -->
    <rect class="panel panel--glue" x="114" y="109" width="67" height="441" fill="var(--tan)" stroke="var(--cutline)" stroke-width="2"/>
    <path class="notch" d="M156,300 L166,310 L166,344 L156,354 Z" fill="var(--paper)"/>

    <!-- front panel -->
    <rect class="panel panel--front" x="182" y="109" width="314" height="441" fill="var(--olive)"/>
    <path class="panel-ornament" role="img" aria-label="Decoratieve bronzen rand met bladmotieven"
          fill-rule="evenodd" fill="var(--bronze)" opacity="0.55"
          d="M193,122 L482,122 L482,530 L193,530 Z M209,140 L466,140 L466,512 L209,512 Z"/>
    <circle class="brand-mark-spot" cx="336" cy="196" r="42" fill="var(--lemon)" role="img" aria-label="Merkteken PLOOIMOES"/>
    <rect class="window-strip" x="242" y="262" width="210" height="229" fill="var(--paper)"/>
    <rect class="name-pill" x="228" y="253" width="222" height="41" rx="14" fill="var(--lemon)"/>
    <text class="brand-word" x="339" y="285" font-size="31" text-anchor="middle" fill="var(--ink)">PLOOIMOES</text>
    <rect class="product-box" x="242" y="294" width="190" height="102" fill="var(--olive)"/>
    <text class="brand-word" x="337" y="322" font-size="28" text-anchor="middle" fill="url(#gold-type)">WASSTRIPS</text>
    <text class="pack-count" x="326" y="354" font-size="30" text-anchor="middle">30</text>
    <g class="strip-bars" stroke="var(--olive)" stroke-width="3">
      <line x1="248" y1="396" x2="248" y2="491"/><line x1="260" y1="396" x2="260" y2="491"/>
      <line x1="272" y1="396" x2="272" y2="491"/><line x1="284" y1="396" x2="284" y2="491"/>
      <line x1="296" y1="396" x2="296" y2="491"/><line x1="308" y1="396" x2="308" y2="491"/>
      <line x1="320" y1="396" x2="320" y2="491"/><line x1="332" y1="396" x2="332" y2="491"/>
      <line x1="344" y1="396" x2="344" y2="491"/><line x1="356" y1="396" x2="356" y2="491"/>
      <line x1="368" y1="396" x2="368" y2="491"/><line x1="380" y1="396" x2="380" y2="491"/>
      <line x1="392" y1="396" x2="392" y2="491"/><line x1="404" y1="396" x2="404" y2="491"/>
      <line x1="416" y1="396" x2="416" y2="491"/><line x1="429" y1="396" x2="429" y2="491"/>
    </g>
    <rect class="contents-box" x="225" y="491" width="227" height="51" fill="var(--olive)" stroke="var(--ink)" stroke-width="2"/>
    <text class="panel-copy" x="339" y="513" font-size="9.5" text-anchor="middle">CONTAINS BEVAT: 30 WASSTRIPS</text>
    <text class="panel-copy" x="339" y="525" font-size="9.5" text-anchor="middle">30 WASSTRIPS = 60 WASBEURTEN</text>

    <!-- narrow side panel -->
    <rect class="panel panel--side" x="496" y="109" width="70" height="441" fill="var(--paper)"/>

    <!-- back panel -->
    <rect class="panel panel--back" x="566" y="111" width="315" height="439" fill="var(--olive)" stroke="var(--cutline)" stroke-width="1.5"/>
    <path class="panel-ornament" role="img" aria-label="Decoratieve bronzen rand rond het venster"
          fill-rule="evenodd" fill="var(--bronze)" opacity="0.55"
          d="M572,121 L878,121 L878,537 L572,537 Z M586,137 L878,137 L878,521 L586,521 Z"/>
    <rect class="panel-ornament-gap" x="586" y="137" width="292" height="384" fill="var(--olive)"/>
    <rect class="view-window" x="612" y="166" width="269" height="331" fill="var(--paper)" stroke="#6a5a4a" stroke-width="1.5"/>

    <!-- tuck flap right -->
    <path class="flap flap--tuck-side" d="M881,111 L932,111 Q945,111 945,124 L945,180 L948,180 L948,450 L945,450 L945,530 Q945,550 925,550 L881,550 Z" fill="var(--olive)"/>
    <path class="tuck-cut" d="M881,163 L902,163 Q928,163 928,200 L928,460 Q928,497 902,497 L881,497 Z" fill="var(--paper)"/>

    <!-- bottom flaps -->
    <path class="flap flap--side-bottom" d="M114,550 L118,606 Q119,614 126,614 L166,614 Q173,614 174,606 L178,556 L181,550 Z" fill="var(--paper)" stroke="var(--cutline)" stroke-width="2"/>
    <path class="flap flap--dust-bottom" d="M184,550 L188,606 Q190,614 200,614 L478,614 Q488,614 490,606 L494,550 Z" fill="var(--paper)" stroke="var(--cutline)" stroke-width="2"/>
    <g class="flap-perforation" stroke="#555" stroke-width="1.5" stroke-dasharray="2 2">
      <line x1="224" y1="566" x2="224" y2="596"/><line x1="242" y1="566" x2="242" y2="596"/>
      <line x1="260" y1="566" x2="260" y2="596"/><line x1="277" y1="566" x2="277" y2="596"/>
      <line x1="295" y1="566" x2="295" y2="596"/><line x1="313" y1="566" x2="313" y2="596"/>
      <line x1="331" y1="566" x2="331" y2="596"/><line x1="349" y1="566" x2="349" y2="596"/>
      <line x1="366" y1="566" x2="366" y2="596"/><line x1="384" y1="566" x2="384" y2="596"/>
      <line x1="402" y1="566" x2="402" y2="596"/><line x1="420" y1="566" x2="420" y2="596"/>
      <line x1="438" y1="566" x2="438" y2="596"/><line x1="455" y1="566" x2="455" y2="596"/>
      <line x1="473" y1="566" x2="473" y2="596"/>
    </g>
    <path class="flap flap--tuck-bottom" d="M496,550 L499,602 Q500,614 512,614 L544,614 Q555,614 556,602 L559,550 Z" fill="var(--tan)" stroke="var(--cutline)" stroke-width="2"/>
    <path class="lid lid--bottom" d="M566,550 L881,550 L869,623 L572,623 Z" fill="var(--olive)" stroke="var(--cutline)" stroke-width="2"/>
    <rect class="name-pill" x="608" y="563" width="218" height="41" rx="14" fill="var(--lemon)"/>
    <text class="brand-word" x="0" y="11" font-size="32" text-anchor="middle" fill="var(--ink)" transform="translate(717 583.5) rotate(180)">PLOOIMOES</text>

    <!-- dimensions -->
    <line class="dim-line" x1="347" y1="641" x2="819" y2="641" stroke="var(--cutline)" stroke-width="2.5"/>
    <text class="spec-label" x="583" y="658" font-size="15" text-anchor="middle" letter-spacing="2">135 MM WIDTH</text>
    <line class="dim-line" x1="1056" y1="110" x2="1056" y2="550" stroke="var(--cutline)" stroke-width="4"/>
    <g class="height-arrow" stroke="var(--arrow)" stroke-width="2.5" fill="none">
      <line x1="1083" y1="122" x2="1083" y2="541"/>
      <polyline points="1073,134 1083,122 1093,134"/>
      <polyline points="1073,529 1083,541 1093,529"/>
    </g>
    <text class="spec-label" x="0" y="0" font-size="17" text-anchor="middle" transform="translate(1076 312) rotate(-90)">185 mm HIGHT</text>
    <text class="spec-label" x="0" y="0" font-size="17" text-anchor="middle" letter-spacing="1.5" transform="translate(1018 362) rotate(-90)">30 MM W X 185 MM H</text>
  </svg>

  <svg class="brand-stage" viewBox="0 681 1200 519" xmlns="http://www.w3.org/2000/svg">
    <defs>
      <radialGradient id="stage-glow" cx="0.49" cy="0.55" r="0.6">
        <stop offset="0" stop-color="#86aabd"/>
        <stop offset="0.45" stop-color="#5d6f66"/>
        <stop offset="1" stop-color="#525e55"/>
      </radialGradient>
    </defs>
    <ellipse class="stage-oval" cx="600" cy="956" rx="506" ry="231" fill="url(#stage-glow)"/>
    <circle class="brand-mark-spot" cx="587" cy="839" r="70" fill="var(--gold)" role="img" aria-label="Merkteken PLOOIMOES"/>
    <text class="brand-word" x="600" y="1072" font-size="118" text-anchor="middle" fill="var(--paper)">PLOOIMOES</text>
  </svg>

</div>
</body>
</html>
```